Brightwell termite & pest control co. needs post card flyer design

we need postcard design for our company targeting residentials.
"House Monthly Special" needs to be the main spotlight then, "No Initial Fee" (with 1 yr or 2 yr monthly/ bi-monthly contract). Licensed, Insured, Bonded must be included as well.
Also, our license # KT7192 needs to show next to the logo.
Our House Monthly Special rate starts from 34.99 (and is based on 1500-2000 SQFT)
Also, 10% off on pest control (Bedbug, Flea, Roach, Ant, Rodent, Bee, Spider, Moth, Fly and many more)
"Mold Licensed" needs to be mentioned.
House Monthly Special needs to be followed by No Initial Fee.
We are not satisfied with the sample postcard I am attaching. please just use the sample as a sample. You do not have to follow the wording on the sample postcard.
Also, the postcard is going to be mailed out. "Local Residential Customer" will be on the address label.
our phone number and web add needs to be on it.
Updates

Project Deadline Extended Reason: We were guaranteed 50 plus designs but not even 10 designs yet........We are still waiting for other designs. Added Monday, November 9, 2015

Project Deadline Extended
Reason: Hello Pixel Forge, We still think it is not enough deigns or designers participating. We still want to see other designs. Ty

Target Market(s)

Residentials

Industry/Entity Type

Pest Control

Requirements
Must have
• House Monthly Special
• NO Initial Fee (with 1 yr or 2yr monthly/bi-monthly contract)
• Starting at $34.99 (In/Out) based on 1500-2000 sqft
• Co Logo, website, 1-800 #, Indicia box (us postage box), Local Residiential Customer (like the sample postcard)
• QR Code
Nice to have
• I have changed my QR Code....
• We would like the customers to know the house monthly special is a special because there is no initial fee. Also, we want $34.99 to stand out......
• We do not want our logo followed by another "brightwell".
Should not have
• Cursive or fancy fonts
• Does not have to follow the sample postcard I am posting.
• Big Saving should not be the main highlight.
• Please remember we want the "House Monthly Special" to be the main.

```html
<!DOCTYPE html>
<html lang="en">
<head>
<meta charset="utf-8">
<title>Brightwell Termite &amp; Pest Control – House Monthly Special</title>
<link href="https://fonts.googleapis.com/css2?family=Oswald:wght@700&family=PT+Sans+Narrow:wght@400;700&family=Archivo:wght@800&display=swap" rel="stylesheet">
<style>
  :root {
    --ink: #3a3441;
    --cream: #fdfbea;
    --olive: #6a7a35;
    --lime: #b4b535;
    --soft-green: #8b9a3c;
    --red: #d9232b;
    --white: #ffffff;
  }
  * { margin: 0; padding: 0; box-sizing: border-box; }
  html, body { width: 1200px; height: 861px; overflow: hidden; background: var(--cream); }
  .postcard { position: relative; width: 1200px; height: 861px; overflow: hidden; background: var(--cream); }
  .backdrop { position: absolute; inset: 0; }

  .mailing { position: absolute; left: 40px; top: 18px; display: flex; gap: 14px; align-items: flex-start; }
  .indicia { width: 112px; height: 70px; border: 2px solid var(--cream); display: flex; flex-direction: column;
    align-items: center; justify-content: center; font-family: "PT Sans Narrow", "Arial Narrow", sans-serif;
    font-size: 13px; line-height: 15px; color: var(--cream); text-align: center; text-transform: uppercase; }
  .address-label { width: 290px; height: 70px; background: var(--white); border-radius: 4px; padding: 12px 16px;
    font-family: "PT Sans Narrow", "Arial Narrow", sans-serif; color: var(--ink); }
  .address-label .recipient { font-weight: 700; font-size: 22px; line-height: 1.1; }
  .address-label .address-line { font-size: 15px; color: #6d6874; }
  .qr-code { width: 84px; height: 84px; background: var(--white); border-radius: 4px; border: 6px solid var(--white);
    outline: 2px solid var(--cream); }
  .site-line { position: absolute; left: 40px; top: 100px; font-family: "PT Sans Narrow", "Arial Narrow", sans-serif;
    font-weight: 700; font-size: 22px; color: var(--cream); display: flex; gap: 12px; align-items: center; }
  .site-line .sep { width: 7px; height: 7px; background: var(--lime); transform: rotate(45deg); }
  .site-line .mold { color: var(--lime); }

  .brand { position: absolute; left: 770px; top: 62px; width: 330px; text-align: center; }
  .brand-name { display: flex; align-items: center; justify-content: center; gap: 10px;
    font-family: "Archivo", Arial, sans-serif; font-weight: 800; font-size: 40px; color: var(--white); letter-spacing: 1px; }
  .brand-dot { width: 16px; height: 16px; border-radius: 50%; background: var(--red); }
  .license { font-family: "Archivo", Arial, sans-serif; font-weight: 800; font-size: 15px; color: var(--white); margin-top: 4px; }
  .brand-tagline { position: absolute; left: 733px; top: 192px; font-family: "Archivo", Arial, sans-serif;
    font-weight: 800; font-size: 21.5px; color: var(--white); letter-spacing: 0.6px; }

  .headline { position: absolute; left: 50px; top: 284px; font-family: "Oswald", "Arial Narrow", sans-serif;
    font-weight: 700; font-size: 62px; color: var(--ink); letter-spacing: -0.5px; line-height: 1; }
  .price-line { position: absolute; left: 50px; top: 360px; display: flex; align-items: baseline; gap: 22px; }
  .price-lead { font-family: "PT Sans Narrow", "Arial Narrow", sans-serif; font-weight: 700; font-size: 46px; color: var(--olive); }
  .price { font-family: "Oswald", "Arial Narrow", sans-serif; font-weight: 700; font-size: 86px; color: var(--red); line-height: 1; letter-spacing: -1px; }
  .price .currency { font-size: 48px; margin-right: 6px; }
  .price-note { position: absolute; left: 50px; top: 452px; font-family: "PT Sans Narrow", "Arial Narrow", sans-serif;
    font-size: 22px; color: var(--soft-green); }
  .fee-title { position: absolute; left: 50px; top: 514px; font-family: "PT Sans Narrow", "Arial Narrow", sans-serif;
    font-weight: 700; font-size: 50px; color: var(--olive); line-height: 1; }
  .fee-terms { position: absolute; left: 50px; top: 574px; font-family: "PT Sans Narrow", "Arial Narrow", sans-serif;
    font-size: 29px; color: var(--soft-green); }

  .pest-badge { position: absolute; left: 662px; top: 309px; width: 222px; height: 222px; }
  .discount-tag { position: absolute; left: 860px; top: 344px; width: 276px; height: 118px; }
  .discount-text { position: absolute; left: 905px; top: 362px; font-family: "PT Sans Narrow", "Arial Narrow", sans-serif;
    font-weight: 700; font-size: 58px; color: var(--white); transform: rotate(2deg); line-height: 1; }
  .discount-text .pct { font-size: 38px; }
  .discount-sub { position: absolute; left: 870px; top: 474px; font-family: "PT Sans Narrow", "Arial Narrow", sans-serif;
    font-size: 55px; color: var(--olive); line-height: 1; }
  .pest-list { position: absolute; left: 688px; top: 556px; width: 475px; font-family: "PT Sans Narrow", "Arial Narrow", sans-serif;
    font-size: 26.5px; line-height: 38px; color: var(--soft-green); }

  .credentials { position: absolute; left: 69px; top: 772px; font-family: "PT Sans Narrow", "Arial Narrow", sans-serif;
    font-weight: 700; font-size: 49px; color: var(--cream); display: flex; align-items: center; gap: 14px; line-height: 1; }
  .credentials .sep { width: 10px; height: 10px; background: var(--cream); transform: rotate(45deg); }
  .phone { position: absolute; right: 52px; top: 760px; font-family: "PT Sans Narrow", "Arial Narrow", sans-serif;
    font-weight: 700; font-size: 70px; color: var(--cream); line-height: 1; }
</style>
</head>
<body>
<main class="postcard">
  <svg class="backdrop" width="1200" height="861" viewBox="0 0 1200 861" aria-hidden="true">
    <path d="M0,150 C300,120 520,200 760,255 C930,295 1080,250 1200,175 V330 H0 Z" fill="var(--olive)"/>
    <path d="M0,195 C300,170 520,240 760,290 C930,320 1080,285 1200,220 V330 H0 Z" fill="var(--cream)"/>
    <path d="M0,205 C250,180 480,250 672,282 C480,275 250,255 0,290 Z" fill="var(--lime)"/>
    <path d="M0,0 H1200 V175 C1090,255 960,272 820,258 C600,235 330,110 0,150 Z" fill="var(--ink)"/>
    <path d="M0,630 C300,690 800,730 1200,690 V861 H0 Z" fill="var(--ink)"/>
    <path d="M0,642 C300,702 800,742 1200,700 V861 H0 Z" fill="var(--lime)"/>
    <path d="M0,690 C400,742 800,748 1200,722 V861 H0 Z" fill="var(--cream)"/>
    <path d="M0,700 C400,752 800,756 1200,732 V861 H0 Z" fill="var(--olive)"/>
  </svg>

  <div class="mailing">
    <div class="indicia"><span>Presorted Std</span><span>US Postage</span><span>Paid</span></div>
    <div class="address-label">
      <div class="recipient">Local Residential Customer</div>
      <div class="address-line">Delivered to current resident</div>
    </div>
    <div class="qr-code" role="img" aria-label="QR code linking to the company website"></div>
  </div>
  <div class="site-line"><span>www.brightwellpest.com</span><span class="sep"></span><span class="mold">Mold Licensed</span></div>

  <div class="brand">
    <div class="brand-name"><span class="brand-dot"></span>BRIGHTWELL</div>
    <div class="license">KT7192</div>
  </div>
  <div class="brand-tagline">TERMITE &amp; PEST CONTROL</div>

  <h1 class="headline">House Monthly Special</h1>
  <div class="price-line">
    <span class="price-lead">starting from</span>
    <span class="price"><span class="currency">$</span>34.99</span>
  </div>
  <p class="price-note">(In/Out, based on 1500-2000 sqft)</p>

  <h2 class="fee-title">No Initial Fee</h2>
  <p class="fee-terms">with 1 or 2 year for monthly or bi-monthly contract</p>

  <svg class="pest-badge" viewBox="0 0 222 222" role="img" aria-label="No-pests sign showing silhouettes of roach, ant, rodent, moth, mosquito and other insects">
    <circle cx="111" cy="111" r="104" fill="#e7e6cf" stroke="var(--red)" stroke-width="12"/>
  </svg>

  <svg class="discount-tag" viewBox="0 0 276 118" aria-hidden="true">
    <polygon points="0,50 40,4 276,12 272,116 36,104" fill="var(--ink)"/>
  </svg>
  <div class="discount-text">•10<span class="pct">%</span> off</div>
  <p class="discount-sub">on pest control</p>
  <p class="pest-list">(Bedbug, Flea, Roach, Ant, Rodent, Bee, Spider, Moth, Fly and many more)</p>

  <div class="credentials">
    <span>Licensed</span><span class="sep"></span><span>Insured</span><span class="sep"></span><span>Bonded</span>
  </div>
  <div class="phone">1-800-555-0147</div>
</main>
</body>
</html>
```